Calm Fern Wellcare- Aged Care and Community Services

Looking for brochure to advertise our services. I will attach a draft that we do not want to use. Looking for graphics that are as natural as possible to present a personalised service. We supply services to aged people and people with disability. Please make it look classy and professional at the same time. I am looking for creativity. I have also attached the logo. Site addresses can be the last page. ideally looking for 2 designs, one A4 and another smaller possibly DL. Looking for creative out of the box thinkers. Thank you.

Target Market(s)

Aged Care service providers, disability service providers and private hospitals

Font styles to use
Serif
Sans Serif
Script

Colors
6b449b
886aae
eea4c8
f59195
fac994
3176b5
0555a3
cedeed
e4daeb

Requirements
Must have
• Targeted imagery, content and contact details
Nice to have
• personal profiles of people happy with our services

```html
<!DOCTYPE html>
<html lang="en">
<head>
<meta charset="utf-8">
<title>Calm Fern Wellcare – Brochure Spread</title>
<link href="https://fonts.googleapis.com/css2?family=Montserrat:ital,wght@0,400;0,500;0,600;1,500;1,600&display=swap" rel="stylesheet">
<style>
  :root {
    --backdrop: #dcdcde;
    --paper: #ede6dc;
    --purple: #6b449b;
    --purple-deep: #5e3a86;
    --lavender: #886aae;
    --lilac: #b49ccb;
    --pink: #eea4c8;
    --rose: #e58fa8;
    --blue: #0555a3;
    --slate: #7b6a94;
    --white: #ffffff;
    --photo-green: #8fae7a;
    --photo-warm: #d9c2a6;
    --photo-sky: #a9c3dc;
  }
  * { box-sizing: border-box; margin: 0; padding: 0; }
  html, body { width: 1200px; height: 840px; overflow: hidden; }
  body {
    background: var(--backdrop);
    font-family: "Montserrat", sans-serif;
    position: relative;
  }
  .spread {
    position: absolute;
    left: 40px; top: 24px;
    width: 1120px; height: 792px;
    display: flex;
    box-shadow: 0 10px 30px rgba(0,0,0,0.18);
  }
  .page {
    position: relative;
    width: 560px; height: 792px;
    background: var(--paper);
    overflow: hidden;
  }
  .page-shapes { position: absolute; inset: 0; }

  .brand-name {
    position: absolute;
    display: flex; align-items: center; gap: 10px;
    color: var(--purple);
    font-weight: 600;
    white-space: nowrap;
  }
  .brand-dot { border-radius: 50%; background: var(--purple); flex: none; }

  /* back page */
  .back .brand-name { left: 200px; top: 98px; font-size: 19px; }
  .back .brand-dot { width: 16px; height: 16px; }
  .vision-label {
    position: absolute; left: 52px; top: 190px;
    width: 90px; text-align: center;
    color: var(--white); font-size: 12px; letter-spacing: 1px; line-height: 1.2;
  }
  .vision-text {
    position: absolute; left: 172px; top: 186px; width: 350px;
    color: var(--purple); font-size: 11.5px; font-style: italic; font-weight: 600;
    line-height: 1.5;
  }
  .contact {
    position: absolute; left: 100px; top: 350px; width: 230px;
    color: var(--white);
  }
  .contact .city { font-size: 13px; color: #e8dcf3; margin-top: 10px; }
  .contact .addr { font-size: 14px; line-height: 1.35; }
  .contact .phone { font-size: 17px; letter-spacing: 1px; margin-top: 6px; }
  .icon { display: block; margin: 0 auto; }
  .footer-note {
    position: absolute; left: 48px; top: 640px; width: 330px;
    color: var(--slate); font-size: 11px; line-height: 1.5;
  }
  .footer-note strong { color: var(--purple); font-weight: 600; display: block; }

  /* front page */
  .front .brand-name { left: 70px; top: 318px; font-size: 20px; }
  .front .brand-dot { width: 18px; height: 18px; }
  .cover-title {
    position: absolute; left: 68px; top: 410px;
    font-weight: 400; font-size: 27px; letter-spacing: 3px; line-height: 1.05;
  }
  .cover-title .line-1 { color: var(--slate); display: block; }
  .cover-title .line-2 { color: var(--blue); display: block; padding-left: 26px; }
  .web-address {
    position: absolute; left: 120px; top: 752px; width: 440px;
    text-align: center; color: var(--white); font-size: 15px; letter-spacing: 1.5px;
  }
</style>
</head>
<body>
<main class="spread">

  <!-- Back page: vision and contact -->
  <section class="page back">
    <svg class="page-shapes" width="560" height="792" viewBox="0 0 560 792">
      <path d="M0 0 H230 C180 60 110 110 0 150 Z" fill="var(--pink)" opacity="0.75"/>
      <path d="M0 0 H185 C140 50 80 90 0 118 Z" fill="var(--lavender)" opacity="0.85"/>

      <circle cx="104" cy="212" r="60" fill="var(--pink)" opacity="0.8"/>
      <circle cx="96" cy="208" r="56" fill="var(--purple)" opacity="0.9"/>

      <path d="M60 470 C40 360 150 300 250 310 C360 320 400 410 370 510 C340 610 220 640 140 610 C80 585 70 530 60 470 Z" fill="var(--pink)" opacity="0.7"/>
      <path d="M70 460 C60 350 160 300 250 300 C350 302 395 390 370 490 C345 590 240 620 160 600 C100 585 78 530 70 460 Z" fill="var(--purple)"/>

      <rect x="470" y="600" width="140" height="230" rx="30" fill="var(--lavender)"/>
      <circle cx="440" cy="705" r="100" fill="var(--pink)" opacity="0.8"/>
      <g role="img" aria-label="Photo of a carer helping a smiling older woman seated in a wheelchair">
        <circle cx="440" cy="705" r="84" fill="var(--photo-sky)"/>
      </g>
    </svg>

    <div class="brand-name"><span class="brand-dot"></span>Calm Fern Wellcare</div>

    <p class="vision-label">THE<br>VISION</p>
    <p class="vision-text">Our vision is to be the most responsive staffing solutions provider in WA, whilst sourcing and placing staff that hold strong values which include ethics, accountability, respect, integrity and adaptability</p>

    <address class="contact" style="font-style:normal">
      <svg class="icon" width="22" height="26" viewBox="0 0 22 26" aria-hidden="true">
        <path d="M11 24 C5 16 2 12 2 9 A9 9 0 0 1 20 9 C20 12 17 16 11 24 Z" fill="none" stroke="var(--white)" stroke-width="2.4"/>
      </svg>
      <p class="city">Perth</p>
      <p class="addr">18 Tamsin Road<br>Oakvale WA 6125</p>
      <p class="city">Adelaide</p>
      <p class="addr">Ground Floor, 41<br>Marlow Street,<br>Elmfield SA 5084</p>
      <svg class="icon" width="26" height="26" viewBox="0 0 26 26" aria-hidden="true" style="margin-top:12px">
        <path d="M6 3 L10 3 L12 8 L9 10 C10 13 13 16 16 17 L18 14 L23 16 L23 20 C23 22 21 23 19 23 C10 22 4 16 3 7 C3 5 4 3 6 3 Z" fill="var(--white)"/>
        <path d="M15 4 A7 7 0 0 1 22 11" fill="none" stroke="var(--white)" stroke-width="1.6"/>
        <path d="M15 8 A3 3 0 0 1 18 11" fill="none" stroke="var(--white)" stroke-width="1.6"/>
      </svg>
      <p class="phone">(08) 9555 0142</p>
    </address>

    <p class="footer-note">For all staff bookings and general enquiries please call us, alternatively, you can email your request or enquiry to <strong>admin@calmfernwellcare.com.au</strong></p>
  </section>

  <!-- Front cover -->
  <section class="page front">
    <svg class="page-shapes" width="560" height="792" viewBox="0 0 560 792">
      <path d="M0 0 H260 C300 120 250 200 330 300 L300 320 C230 230 200 140 0 70 Z" fill="var(--lilac)"/>
      <path d="M0 0 H200 C220 100 240 180 300 270 C200 200 120 120 0 90 Z" fill="var(--lavender)"/>
      <path d="M0 0 H110 C140 60 170 110 240 170 C140 140 60 90 0 60 Z" fill="var(--purple)"/>
      <path d="M270 280 C230 360 240 440 300 520 L330 520 C280 440 270 360 300 290 Z" fill="var(--rose)" opacity="0.85"/>
      <path d="M420 620 C470 650 520 700 560 720 V600 Z" fill="var(--pink)"/>
      <path d="M470 640 C500 660 530 690 560 705 V640 Z" fill="var(--purple)"/>

      <g role="img" aria-label="Photo of a male carer giving a high five to an older woman outdoors">
        <path d="M300 40 H560 V330 H300 C270 240 270 130 300 40 Z" fill="var(--photo-green)"/>
      </g>
      <g role="img" aria-label="Photo of a nurse walking arm in arm with a laughing older woman indoors">
        <path d="M296 340 H560 V560 H360 C320 500 295 420 296 340 Z" fill="var(--photo-warm)"/>
      </g>
      <g role="img" aria-label="Photo of older residents playing cards with a carer at an outdoor table">
        <path d="M140 600 H560 V792 H110 L130 640 C132 615 135 605 140 600 Z" fill="var(--photo-green)" opacity="0.85"/>
      </g>
      <path d="M100 740 H560 V792 H92 Z" fill="var(--purple)"/>
    </svg>

    <div class="brand-name"><span class="brand-dot"></span>Calm Fern Wellcare</div>

    <h1 class="cover-title">
      <span class="line-1">REIMAGINING</span>
      <span class="line-2">HEALTHCARE</span>
    </h1>

    <p class="web-address">www.calmfernwellcare.com.au</p>
  </section>

</main>
</body>
</html>
```